TalkBridge - Language Coaching Services

Sleek, innovative, trendy design for Language Coaching business.

TalkBridge is a new UK based company that provides Language Coaching services. We offer highly personalized on-line and face to face language courses. We also impart learning techniques workshops based on the latest neuroscience research for second-language acquisition.

Target Market(s)

Industry/Entity Type

Consulting

Contact Information for Business Card

TalkBridge
ElenaVT@talkbridge-demo.co.uk
TalkBridge-demo.co.uk
London, UK

Font styles to use
Sans Serif

```html
<!DOCTYPE html>
<html lang="en">
<head>
<meta charset="utf-8">
<title>TalkBridge Business Card</title>
<link rel="stylesheet" href="https://fonts.googleapis.com/css2?family=Open+Sans:wght@300;400;700&display=swap">
<style>
  :root {
    --backdrop: #2b2b2b;
    --card: #f7f7f7;
    --brand-blue: #1583bd;
    --band-blue: #1480b8;
    --ink-grey: #555a5e;
    --white: #ffffff;
  }
  * { margin: 0; padding: 0; box-sizing: border-box; }
  html, body {
    width: 1200px; height: 892px; overflow: hidden;
    background: var(--backdrop);
    font-family: "Open Sans", Arial, sans-serif;
  }
  .stage {
    width: 1200px; height: 892px;
    display: flex; flex-direction: column; align-items: center; justify-content: center;
    gap: 44px;
  }
  .card {
    position: relative;
    width: 660px; height: 377px;
    background: var(--card);
    box-shadow: 0 10px 30px rgba(0,0,0,.45);
    overflow: hidden;
  }
  /* Front face */
  .card-front {
    display: flex; flex-direction: column; align-items: center;
    padding-top: 78px;
  }
  .brand-dot {
    width: 92px; height: 92px; border-radius: 50%;
    background: var(--brand-blue);
  }
  .brand-name {
    margin-top: 20px;
    font-size: 40px; font-weight: 400; letter-spacing: 3px;
    color: var(--brand-blue);
  }
  .website {
    margin-top: 54px;
    font-size: 15px; letter-spacing: 7px;
    color: var(--ink-grey);
    white-space: nowrap;
  }
  /* Back face */
  .wordmark {
    position: absolute; top: 82px; left: 0; right: 0;
    text-align: center;
    font-size: 66px; font-weight: 400; letter-spacing: 4px;
    color: var(--brand-blue);
    white-space: nowrap;
  }
  .contact-band {
    position: absolute; left: 0; right: 0; top: 232px; height: 96px;
    background: var(--band-blue);
    color: var(--white);
  }
  .holder {
    position: absolute; left: 60px; bottom: 14px;
    white-space: nowrap;
  }
  .holder-name { font-size: 22px; font-weight: 700; line-height: 1.1; }
  .holder-role { font-size: 16px; font-weight: 400; }
  .band-dot {
    position: absolute; left: 322px; top: 50%; transform: translateY(-50%);
    width: 78px; height: 78px; border-radius: 50%;
    background: var(--band-blue);
    border: 4px solid var(--white);
  }
  .contact-list {
    position: absolute; right: 24px; top: 16px;
    list-style: none; text-align: right;
    font-size: 15px; line-height: 1.7;
  }
  .contact-list li {
    display: flex; align-items: center; justify-content: flex-end; gap: 10px;
    white-space: nowrap;
  }
  .contact-list svg { width: 15px; height: 15px; flex: none; fill: none; stroke: var(--white); stroke-width: 1.8; }
</style>
</head>
<body>
<main class="stage">
  <section class="card card-front" aria-label="Card front">
    <div class="brand-dot"></div>
    <div class="brand-name">TALKBRIDGE</div>
    <div class="website">www.talkbridge-demo.co.uk</div>
  </section>

  <section class="card card-back" aria-label="Card back">
    <div class="wordmark">TALKBRIDGE</div>
    <div class="contact-band">
      <div class="holder">
        <div class="holder-name">ELENA VARGA</div>
        <div class="holder-role">PRESIDENT</div>
      </div>
      <div class="band-dot"></div>
      <ul class="contact-list">
        <li>020 7946 0312
          <svg viewBox="0 0 16 16" aria-hidden="true"><rect x="4" y="1.5" width="8" height="13" rx="1.5"/><line x1="7" y1="12" x2="9" y2="12"/></svg>
        </li>
        <li>info@talkbridge-demo.co.uk
          <svg viewBox="0 0 16 16" aria-hidden="true"><rect x="1.5" y="3.5" width="13" height="9"/><polyline points="1.5,3.5 8,9 14.5,3.5"/></svg>
        </li>
      </ul>
    </div>
  </section>
</main>
</body>
</html>
```